the theater production needs a poster design

we
we need a poster design for the Opera 'Tobin and Marigold'
the show will be put on the stage on May 18.
the week is family week.
we launch the Opera on the stage size of 700 people
the opera will be performed by Orchestra of 30 musicians and 7 singers
most of audience are parents with children.
we will use the final design for the printing and mobile marketing.

here is the informations

Opera 'Tobin and Marigold'

date: 2024.5.18 Saturday 2pm, 5pm
Seoryeon Arthall
Ticket $50
BOOK _02-735-6089
Music Director_Yuna Seo, Producer Taeho Park

```html
<!DOCTYPE html>
<html lang="en">
<head>
<meta charset="utf-8">
<title>Opera Tobin and Marigold – Poster</title>
<link rel="stylesheet" href="https://fonts.googleapis.com/css2?family=Rye&family=Dancing+Script:wght@600&family=Poppins:wght@400;500;600;700;800&family=Montserrat:wght@900&family=Roboto+Condensed:wght@400&display=swap">
<style>
  :root {
    --paper: #ffffff;
    --night: #0d0f0b;
    --forest-deep: #141a10;
    --forest-mid: #26321b;
    --peach: #f6c4a4;
    --peach-soft: #f9cfb3;
    --gold: #c7a53a;
    --ink: #0a0a0a;
    --label-dark: #2a241d;
    --white: #ffffff;
  }
  * { margin: 0; padding: 0; box-sizing: border-box; }
  html, body { width: 880px; height: 1200px; overflow: hidden; background: var(--paper); }
  .poster {
    position: absolute; left: 14px; top: 14px; width: 852px; height: 1172px;
    overflow: hidden; background: var(--night);
  }
  .forest-art {
    position: absolute; inset: 0 0 420px 0;
    background:
      radial-gradient(ellipse 200px 180px at 330px 590px, rgba(110,50,40,.45), transparent 70%),
      radial-gradient(ellipse 500px 420px at 460px 300px, var(--forest-mid), transparent 75%),
      linear-gradient(180deg, var(--forest-deep) 0%, #1d2615 60%, var(--night) 100%);
  }
  .orchestra-art {
    position: absolute; left: 0; right: 0; bottom: 0; height: 440px;
    background:
      radial-gradient(ellipse 300px 160px at 640px 190px, rgba(120,60,25,.55), transparent 70%),
      radial-gradient(ellipse 260px 120px at 130px 240px, rgba(90,45,20,.45), transparent 70%),
      linear-gradient(180deg, transparent 0%, rgba(30,18,10,.85) 30%, #120c08 100%);
  }
  .notes-art {
    position: absolute; left: 0; top: 14px; width: 200px; height: 460px;
    background: linear-gradient(160deg, rgba(30,150,130,.35) 0%, rgba(200,60,50,.3) 50%, rgba(230,150,40,.35) 80%, transparent 100%);
    border-radius: 0 120px 160px 0;
    filter: blur(6px);
  }
  .kicker {
    position: absolute; left: 92px; top: 118px;
    font-family: "Dancing Script", cursive; font-weight: 600;
    font-size: 86px; color: var(--peach); transform: rotate(-8deg);
  }
  .title-line {
    position: absolute; left: 0; width: 852px; text-align: center;
    font-family: "Rye", serif; color: var(--white);
    text-shadow: 5px 5px 0 var(--gold);
  }
  .title-first { top: 206px; font-size: 108px; left: 20px; }
  .title-and { top: 344px; font-size: 24px; text-shadow: 2px 2px 0 var(--gold); left: 0; }
  .title-second { top: 384px; font-size: 84px; left: 0; }
  .rule { position: absolute; top: 341px; height: 1.5px; width: 110px; background: var(--white); }
  .rule-left { left: 249px; } .rule-right { left: 497px; }
  .ticket {
    position: absolute; left: 217px; top: 670px; width: 390px; height: 130px;
    transform: rotate(-4deg); transform-origin: left bottom;
  }
  .ticket-box {
    position: absolute; inset: 0 0 30px 0; background: var(--peach-soft); border-radius: 10px;
    display: flex; align-items: center; justify-content: center; gap: 10px;
  }
  .ticket-label { font-family: "Poppins", sans-serif; font-weight: 500; font-size: 44px; color: var(--ink); }
  .ticket-price { font-family: "Montserrat", sans-serif; font-weight: 900; font-size: 72px; color: var(--ink); }
  .booking {
    position: absolute; left: 34px; top: 90px; padding: 2px 14px 4px;
    background: var(--label-dark); border-radius: 4px;
    font-family: "Roboto Condensed", sans-serif; font-size: 34px; color: var(--peach);
  }
  .date-block { position: absolute; left: 82px; top: 864px; width: 310px; text-align: center; }
  .day { font-family: "Poppins", sans-serif; font-size: 28px; letter-spacing: 9px; color: var(--peach); }
  .date { font-family: "Poppins", sans-serif; font-weight: 700; font-size: 96px; line-height: 1; color: var(--white); margin-top: 4px; }
  .time { font-family: "Poppins", sans-serif; font-size: 40px; color: var(--peach); margin-top: 6px; }
  .divider { position: absolute; left: 417px; top: 850px; width: 1.5px; height: 214px; background: var(--peach); }
  .credits { position: absolute; left: 465px; top: 878px; color: var(--white); font-family: "Poppins", sans-serif; }
  .credit-role { font-size: 21px; font-weight: 500; }
  .credit-name { font-size: 37px; font-weight: 700; line-height: 1.1; margin-bottom: 22px; }
  .venue {
    position: absolute; left: 0; width: 852px; top: 1084px;
    display: flex; justify-content: center; align-items: center; gap: 12px;
    font-family: "Poppins", sans-serif; font-weight: 600; font-size: 27px; color: var(--white);
  }
</style>
</head>
<body>
<main class="poster">
  <div class="forest-art" role="img" aria-label="Painted dark forest with two children embracing"></div>
  <div class="orchestra-art" role="img" aria-label="Orchestra violinists playing in warm low light"></div>
  <div class="notes-art" role="img" aria-label="Colourful flowing music notes"></div>

  <div class="kicker">Opera</div>
  <h1>
    <span class="title-line title-first">TOBIN</span>
    <span class="rule rule-left"></span><span class="rule rule-right"></span>
    <span class="title-line title-and">AND</span>
    <span class="title-line title-second">MARIGOLD</span>
  </h1>

  <div class="ticket">
    <div class="ticket-box">
      <span class="ticket-label">Ticket</span>
      <span class="ticket-price">$50</span>
    </div>
    <div class="booking">BOOK 02-735-6089</div>
  </div>

  <div class="date-block">
    <div class="day">SATURDAY</div>
    <div class="date">18/05</div>
    <div class="time">2PM - 5PM</div>
  </div>

  <div class="divider"></div>

  <div class="credits">
    <div class="credit-role">Music Director</div>
    <div class="credit-name">YUNA SEO</div>
    <div class="credit-role">Producer</div>
    <div class="credit-name">TAEHO PARK</div>
  </div>

  <div class="venue">
    <svg width="22" height="30" viewBox="0 0 22 30" aria-hidden="true">
      <path d="M11 0C4.9 0 0 4.9 0 11c0 8 11 19 11 19s11-11 11-19C22 4.9 17.1 0 11 0z" fill="#f6c4a4"/>
      <circle cx="11" cy="11" r="4.5" fill="#120c08"/>
    </svg>
    <span>Venue: Seoryeon Arthall</span>
  </div>
</main>
</body>
</html>
```